Postcard Design

I need a postcard/flyer designed to advertise my nail business. I am qualified with Palm and Polish Guild UK and insured with CORVEL. I am offering Lustrik nail

I am fully mobile with flexible appointments. Beautiful nails for up to 3 weeks. No chipping, dulling or fading.

Prices: Fingernails £20. Toenails £20. Both for £35. Gel removal £10

Call Brenda on 07812604117 or email lustrik_tips@mailbox-example.com can also follow on Chirper @Lustrik_tips.

Was hoping for a colourful and classy design, maybe a bit vintage that will appeal to all ages. Especially for weddings/honeymoons. Doesnt necessarily have to feature pictures of manicures/pedicures/hands/feet etc.

hope this all makes sense!

Brenda

Industry/Entity Type

Business

Font styles to use
Serif

Colors
e567a6
34b8a4
33a6d7
b768aa
86cfc6
f04a50
d3a5cc

```html
<!DOCTYPE html>
<html lang="en">
<head>
<meta charset="utf-8">
<title>Lustrik Nail – Postcard</title>
<link rel="stylesheet" href="https://fonts.googleapis.com/css2?family=Comfortaa:wght@700&family=Federant&family=Fira+Sans:wght@500&display=swap">
<style>
  :root {
    --paper-light: #efd3ad;
    --paper-mid: #e6c199;
    --paper-dark: #d9a87c;
    --title: #8e1f45;
    --ink: #2e1a2a;
    --contact: #6b2a6e;
    --hand: #c98a5a;
    --portrait: #9d7c5e;
    --ticket: #e9a3b4;
    --scene: #b9a184;
    --boot: #6fbcb4;
    --bouquet: #8fb79a;
    --ribbon-pink: #c65fb3;
    --ribbon-blue: #5fb6d6;
    --ribbon-lime: #c9d65a;
    --ribbon-coral: #ee8a6a;
  }
  html, body {
    margin: 0;
    padding: 0;
    width: 1200px;
    height: 924px;
    overflow: hidden;
    background: #ffffff;
  }
  .postcard {
    position: relative;
    width: 1200px;
    height: 924px;
    overflow: hidden;
    background: radial-gradient(ellipse at 30% 40%, var(--paper-light) 0%, var(--paper-mid) 60%, var(--paper-dark) 100%);
    font-family: "Federant", serif;
  }
  .artwork {
    position: absolute;
    display: block;
  }
  .artwork--hand {
    left: 518px; top: 48px; width: 262px; height: 150px;
    border-radius: 40% 50% 45% 35%;
    background: radial-gradient(ellipse at 45% 55%, var(--hand) 0%, #dba888 70%, transparent 100%);
  }
  .artwork--portrait {
    left: 952px; top: 25px; width: 210px; height: 325px;
    background: linear-gradient(160deg, #7d5b45 0%, var(--portrait) 45%, #c9b196 100%);
  }
  .artwork--ticket {
    left: 1002px; top: 292px; width: 198px; height: 110px;
    transform: rotate(-12deg);
    background: var(--ticket);
    opacity: 0.85;
  }
  .artwork--scene {
    left: 28px; top: 682px; width: 270px; height: 212px;
    background: linear-gradient(135deg, #8f7559 0%, var(--scene) 55%, #d8c6a8 100%);
  }
  .artwork--boot {
    left: 262px; top: 565px; width: 178px; height: 325px;
    border-radius: 45% 45% 20% 20%;
    background: linear-gradient(180deg, #b98844 0%, #c69a4e 30%, var(--boot) 45%, var(--boot) 100%);
  }
  .artwork--bouquet {
    left: 930px; top: 592px; width: 215px; height: 132px;
    border-radius: 50% 50% 30% 30%;
    background: linear-gradient(180deg, var(--bouquet) 0%, #a7c9a9 65%, #e36d6a 100%);
  }
  .artwork--ribbon {
    left: 690px; top: 836px; width: 505px; height: 66px;
    border-radius: 30px;
    background: linear-gradient(180deg, var(--ribbon-pink) 0%, var(--ribbon-blue) 40%, var(--ribbon-lime) 65%, var(--ribbon-coral) 100%);
    opacity: 0.9;
  }
  .brand-title {
    position: absolute;
    left: 115px; top: 94px;
    margin: 0;
    font-family: "Comfortaa", sans-serif;
    font-weight: 700;
    font-size: 60px;
    line-height: 1;
    color: var(--title);
    letter-spacing: 1px;
  }
  .tagline {
    position: absolute;
    left: 175px; top: 204px;
    margin: 0;
    font-size: 39px;
    line-height: 52px;
    color: var(--ink);
    letter-spacing: 1px;
  }
  .contact {
    position: absolute;
    left: 175px; top: 397px;
    margin: 0;
    font-size: 39px;
    line-height: 51px;
    color: var(--contact);
    letter-spacing: 1px;
  }
  .contact .detail {
    font-family: "Fira Sans", sans-serif;
    font-weight: 500;
    font-size: 37px;
    letter-spacing: 0.5px;
  }
  .price-list {
    position: absolute;
    left: 605px; top: 622px;
    margin: 0;
    font-size: 38px;
    line-height: 50px;
    color: var(--ink);
    border-collapse: collapse;
  }
  .price-list th {
    text-align: left;
    font-weight: normal;
    padding: 0;
  }
  .price-list td { padding: 0; }
  .price-list .item { width: 257px; }
</style>
</head>
<body>
<main class="postcard">
  <div class="artwork artwork--hand" role="img" aria-label="Vintage illustration of a hand holding a pink rose"></div>
  <div class="artwork artwork--portrait" role="img" aria-label="Sepia vintage portrait illustration of a woman"></div>
  <div class="artwork artwork--ticket" role="img" aria-label="Pink admission ticket stub"></div>
  <div class="artwork artwork--scene" role="img" aria-label="Sepia vintage illustration of a group of ladies"></div>
  <div class="artwork artwork--boot" role="img" aria-label="Vintage turquoise lace-up boot filled with golden roses"></div>
  <div class="artwork artwork--bouquet" role="img" aria-label="Bouquet of lily of the valley in a red dish"></div>
  <div class="artwork artwork--ribbon" role="img" aria-label="Multicoloured wavy ribbon ornament in pink, blue, lime and coral"></div>

  <h1 class="brand-title">Lustrik Nail</h1>

  <p class="tagline">
    Beautiful nails for up to three weeks.<br>
    No chipping, dulling or fading.
  </p>

  <p class="contact">
    Call BRENDA on <span class="detail">07812604117</span><br>
    or email <span class="detail">lustrik_tips@mailbox-example.com</span><br>
    can also follow on <span class="detail">Chirper@Lustrik_tips.</span>
  </p>

  <table class="price-list">
    <tr><th colspan="2">Prices:</th></tr>
    <tr><td class="item">Fingernails</td><td>£20</td></tr>
    <tr><td class="item">Toenails</td><td>£20</td></tr>
    <tr><td class="item">Gel Removal</td><td>£10</td></tr>
  </table>
</main>
</body>
</html>
```